Webpage

I am a professional genealogist. I need a webpage that is professional looking (using the logo I chose), I can add hyperlinks and photos to if and when I want.

```html
<!DOCTYPE html>
<html lang="en">
<head>
<meta charset="utf-8">
<title>Lineage Trail Research</title>
<link rel="stylesheet" href="https://fonts.googleapis.com/css2?family=Questrial&family=Roboto+Condensed:wght@400&family=Noto+Serif:ital@0;1&family=Arimo:wght@400&display=swap">
<style>
  :root {
    --teal: #17acc3;
    --teal-dark: #1597ad;
    --green: #2f8f6c;
    --ink: #333333;
    --body-text: #505050;
    --footer-bg: #4b4b4b;
    --footer-line: #d5d8d8;
    --footer-text: #d6d6d6;
    --icon-grey: #7d7d7d;
    --white: #ffffff;
  }
  * { box-sizing: border-box; margin: 0; padding: 0; }
  html, body { width: 960px; height: 1200px; overflow: hidden; }
  body {
    position: relative;
    font-family: "Arimo", Arial, sans-serif;
    color: var(--ink);
    background: #ffffff;
  }
  .backdrop {
    position: absolute; left: 0; top: 0; width: 960px; height: 720px;
    background: linear-gradient(180deg, #5e9bd3 0%, #8fbfe5 30%, #c9def0 55%, #eef4f9 80%, #ffffff 100%);
  }
  .page {
    position: absolute; left: 96px; top: 0; width: 768px; height: 1013px;
    background: linear-gradient(180deg, rgba(255,255,255,0.92) 0%, rgba(255,255,255,0.95) 60%, #ffffff 100%);
  }
  .site-header { position: absolute; left: 0; top: 0; width: 768px; height: 138px; border-bottom: 3px solid #dfe3e4; }
  .brand { position: absolute; left: 262px; top: 30px; display: flex; align-items: center; gap: 12px; }
  .brand-dot { width: 62px; height: 62px; border-radius: 50%; background: #8fcfb3; }
  .brand-name { font-family: "Questrial", sans-serif; font-size: 22px; color: #4a4a4a; line-height: 1.1; width: 150px; }
  .social-top { position: absolute; right: 12px; top: 14px; display: flex; gap: 5px; }
  .social-top span { width: 19px; height: 19px; border-radius: 50%; background: var(--icon-grey); }
  .call { position: absolute; right: 12px; top: 38px; font-family: "Questrial", sans-serif; font-size: 21px; color: var(--teal); }
  .call strong { font-weight: 700; }
  .main-nav {
    position: absolute; left: 0; top: 141px; width: 768px; height: 37px;
    background: var(--teal); display: flex; justify-content: center; gap: 32px; align-items: center;
  }
  .main-nav a { font-family: "Questrial", sans-serif; color: var(--white); text-decoration: none; font-size: 14px; letter-spacing: 0.2px; }
  .hero {
    position: absolute; left: 0; top: 181px; width: 768px; height: 286px;
    background: linear-gradient(120deg, #5b4a3e 0%, #8a7a6c 35%, #cfcac4 60%, #e9e3dc 80%, #a48a6e 100%);
  }
  .hero-caption {
    position: absolute; left: 0; width: 768px; top: 238px; text-align: center;
    font-family: "Arimo", sans-serif; font-size: 28px; color: var(--white);
    text-shadow: 0 1px 3px rgba(0,0,0,0.7);
  }
  .welcome { position: absolute; left: 0; top: 467px; width: 768px; height: 68px; text-align: center; background: rgba(236,243,247,0.7); }
  .welcome h1 { font-family: "Roboto Condensed", sans-serif; font-weight: 400; font-size: 33px; color: var(--teal); margin-top: 14px; line-height: 1; }
  .welcome p { font-size: 15px; color: var(--ink); margin-top: 4px; }
  .intro-image {
    position: absolute; left: 12px; top: 548px; width: 212px; height: 152px;
    background: linear-gradient(135deg, #d9cfc8 0%, #a89283 50%, #4c3f38 100%);
  }
  .intro-text { position: absolute; left: 240px; top: 568px; width: 516px; font-size: 12.3px; line-height: 19px; color: var(--body-text); }
  .intro-text p + p { margin-top: 19px; }
  .section-title { font-family: "Roboto Condensed", sans-serif; font-weight: 400; font-size: 27px; color: var(--green); line-height: 1; }
  .services { position: absolute; left: 12px; top: 732px; width: 480px; }
  .services > p { margin-top: 14px; font-size: 12.3px; line-height: 20px; color: var(--body-text); }
  .service-list { list-style: none; margin-top: 28px; display: grid; grid-template-columns: 240px 240px; grid-auto-flow: column; grid-template-rows: repeat(3, 25.5px); font-size: 13.5px; color: #222; }
  .service-list li { position: relative; padding-left: 12px; }
  .service-list li::before { content: ""; position: absolute; left: 0; top: 5px; width: 6px; height: 6px; border-radius: 50%; background: var(--teal); }
  .testimonials { position: absolute; left: 525px; top: 732px; width: 235px; }
  .testimonials blockquote { margin-top: 16px; font-family: "Noto Serif", serif; font-style: italic; font-size: 12.6px; line-height: 19.3px; color: #333; }
  .testimonial-name { margin-top: 12px; font-family: "Noto Serif", serif; font-size: 15px; color: #222; }
  .testimonial-place { font-family: "Noto Serif", serif; font-size: 12px; color: #222; margin-top: 2px; }
  .site-footer { position: absolute; left: 0; top: 1013px; width: 960px; height: 187px; background: var(--footer-bg); border-top: 5px solid var(--footer-line); color: var(--footer-text); }
  .footer-title { position: absolute; left: 108px; top: 18px; font-family: "Questrial", sans-serif; font-size: 16px; color: var(--white); letter-spacing: 0.3px; }
  .portrait { position: absolute; left: 107px; top: 51px; width: 46px; height: 46px; border: 2px solid #d0d0d0; background: linear-gradient(180deg, #b9b4ae, #7b7671); }
  .person { position: absolute; left: 163px; top: 55px; color: var(--white); }
  .person .name { font-family: "Questrial", sans-serif; font-size: 15px; }
  .person .role { font-size: 12px; margin-top: 5px; }
  .contact-line { position: absolute; display: flex; gap: 8px; font-size: 12.3px; line-height: 19px; }
  .contact-line svg { flex: none; margin-top: 2px; }
  .social-foot { position: absolute; right: 108px; top: 20px; display: flex; gap: 6px; }
  .social-foot span { width: 27px; height: 27px; border-radius: 50%; background: var(--icon-grey); }
  .foot-nav { position: absolute; right: 108px; top: 86px; width: 260px; text-align: right; font-family: "Questrial", sans-serif; font-size: 11px; line-height: 18px; color: var(--white); }
  .foot-nav a { color: var(--white); text-decoration: none; }
  .foot-nav .sep { margin: 0 8px; }
  .copyright { position: absolute; right: 108px; top: 133px; text-align: right; font-size: 11.5px; line-height: 16px; color: #c8c8c8; }
</style>
</head>
<body>
  <div class="backdrop" role="img" aria-label="Snowy mountain range under a blue sky"></div>

  <div class="page">
    <header class="site-header">
      <div class="brand">
        <span class="brand-dot"></span>
        <span class="brand-name">Lineage Trail Research</span>
      </div>
      <div class="social-top"><span></span><span></span><span></span></div>
      <div class="call">Call: <strong>512-555-0148</strong></div>
    </header>

    <nav class="main-nav">
      <a href="#">HOME</a><a href="#">ABOUT</a><a href="#">SERVICES</a><a href="#">PUBLICATIONS</a><a href="#">BLOG</a><a href="#">LINKS</a><a href="#">CONTACT</a>
    </nav>

    <section class="hero" role="img" aria-label="Photo of an older woman and a young woman talking over flowers">
      <div class="hero-caption">Maecenas ultrices eros eget justo ultricies</div>
    </section>

    <section class="welcome">
      <h1>WELCOME</h1>
      <p>Maecenas ultrices eros eget justo ultricies</p>
    </section>

    <div class="intro-image" role="img" aria-label="Open family history book with old photographs"></div>
    <div class="intro-text">
      <p>Maecenas ultrices eros eget justo ultricies in mollis augue commodo. Nullam sem tortor, volutpat non eleifend ut, adipiscing in augue. Aliquam at eros magna.</p>
      <p>Etiam tempus est quis massa sagittis sit amet lobortis quam malesuada. In interdum blandit ornare. Vivamus malesuada arcu in tellus consectetur rhoncus. Lorem ipsum dolor sit amet, consectetur adipiscing elit. Pellentesque rhoncus magna in tellus luctus gravida. Donec nisl diam, imperdiet eu pulvinar eget, faucibus eu mi.</p>
    </div>

    <section class="services">
      <h2 class="section-title">Our Services</h2>
      <p>Maecenas ultrices eros eget justo ultricies in mollis augue commodo. Nullam sem tortor, volutpat non eleifend ut, adipiscing in augue.</p>
      <ul class="service-list">
        <li>Forensic Genealogy,</li>
        <li>Kinship Determination,</li>
        <li>Research Analysis and Consultation,</li>
        <li>Texas Researcher,</li>
        <li>Record Retrieval.</li>
      </ul>
    </section>

    <section class="testimonials">
      <h2 class="section-title">Clients Testimonials</h2>
      <blockquote>Lorem ipsum dolor sit amet, consectetur adipiscing elit. Ut sit amet metus ut lorem pharetra venenatis fermentum at nibh. Nulla aliquet diam eu turpis convallis sit amet malesuada mi ultrices. In in velit massa, vitae condimentum leo. Vivamus nulla sapien, bibendum eget malesuada eget, volutpat nec nisl.</blockquote>
      <div class="testimonial-name">Jhon Doe</div>
      <div class="testimonial-place">Chicago, USA</div>
    </section>
  </div>

  <footer class="site-footer">
    <div class="footer-title">LINEAGE TRAIL RESEARCH</div>
    <div class="portrait" role="img" aria-label="Portrait of the genealogist"></div>
    <div class="person">
      <div class="name">Dana Whitcomb,</div>
      <div class="role">Professional Genealogist</div>
    </div>
    <div class="contact-line" style="left:110px; top:116px;">
      <svg width="11" height="15" viewBox="0 0 11 15"><path d="M5.5 0C2.5 0 0 2.4 0 5.4 0 9.4 5.5 15 5.5 15S11 9.4 11 5.4C11 2.4 8.5 0 5.5 0zm0 7.6a2.2 2.2 0 110-4.4 2.2 2.2 0 010 4.4z" fill="#17acc3"/></svg>
      <span>PO Box 40417<br>Austin, TX 78760-0417</span>
    </div>
    <div class="contact-line" style="left:346px; top:110px;">
      <svg width="10" height="16" viewBox="0 0 10 16"><rect x="0.5" y="0.5" width="9" height="15" rx="1.5" fill="#17acc3"/><rect x="2" y="2.5" width="6" height="9" fill="#4b4b4b"/><circle cx="5" cy="13.5" r="0.9" fill="#4b4b4b"/></svg>
      <span>512-555-0148</span>
    </div>
    <div class="contact-line" style="left:346px; top:135px;">
      <svg width="14" height="10" viewBox="0 0 14 10" style="margin-top:4px"><rect width="14" height="10" rx="1" fill="#17acc3"/><path d="M0.5 0.8L7 5.6 13.5 0.8" stroke="#4b4b4b" stroke-width="1.2" fill="none"/></svg>
      <span>dana@lineagetrail.example</span>
    </div>
    <div class="social-foot"><span></span><span></span><span></span></div>
    <nav class="foot-nav">
      <a href="#">HOME</a><span class="sep">|</span><a href="#">ABOUT</a><span class="sep">|</span><a href="#">SERVICES</a><span class="sep">|</span><a href="#">PUBLICATIONS</a><br>
      <a href="#">BLOG</a><span class="sep">|</span><a href="#">LINKS</a><span class="sep">|</span><a href="#">CONTACT</a>
    </nav>
    <div class="copyright">Copyright © 2014 Lineage Trail Research.<br>All Rights Reserved.</div>
  </footer>
</body>
</html>
```